GLS biz card

We need a business card design for our new company based in Los Angeles called "Gold Lantern Studios". We develop film and television projects. We work with investors, financiers, film production companies, film distribution and sales companies as well as studios. We would like to incorporate our logo (see attached) on a two-sided card. We need to include: name and title, address, phone, email and company website.

Target Market(s)

Business, financial and studio clients

Industry/Entity Type

Business

Contact Information for Business Card

Two-sided. We are thinking of the logo on one side and the information on the back. Please feel free to be creative! Thanks.

Requirements
Must have
• Please include the following text information, excluding the "CAPS CATEGORY:" and please allow the ability for us to change the name, title and email address for each company employee):
• NAME & TITLE:
• Peter Dunmore
• Managing Partner
• COMPANY NAME:
• GOLD LANTERN STUDIOS (please use existing logo)
• COMPANY ADDRESS:
• KVT Arts Park
• 2480 Wexley Boulevard
• Arts Hall, 4th Floor
• Manhattan Beach, CA 90266
• COMPANY PHONE NUMBER:
• 310-555-4206
• COMPANY WEBSITE ADDRESS:
• www.goldlanternstudioshouse.com
• EMAIL ADDRESS: (only one per card)
• frank@goldlanternstudioshouse.com
• tizzy@goldlanternstudioshouse.com
• peter@goldlanternstudioshouse.com

```html
<!DOCTYPE html>
<html lang="en">
<head>
<meta charset="utf-8">
<title>Gold Lantern Studios – Business Card</title>
<link href="https://fonts.googleapis.com/css2?family=Jura:wght@400;600&family=Arimo:wght@400&display=swap" rel="stylesheet">
<style>
  :root {
    --backdrop: #d9d9d9;
    --card: #000000;
    --accent: #29b8e8;
    --accent-soft: #7fd6f2;
    --accent-glint: #eaf9ff;
    --text-light: #f2f2f2;
  }
  * { margin: 0; padding: 0; box-sizing: border-box; }
  html, body {
    width: 1200px;
    height: 900px;
    overflow: hidden;
    background: var(--backdrop);
  }
  .canvas {
    position: relative;
    width: 1200px;
    height: 900px;
  }
  .card {
    position: absolute;
    left: 320px;
    width: 560px;
    height: 320px;
    background: var(--card);
    overflow: hidden;
    box-shadow: 0 6px 18px rgba(0,0,0,0.35);
  }
  .card--front { top: 90px; }
  .card--back { top: 470px; }

  .band {
    position: absolute;
    height: 8px;
    background: linear-gradient(90deg, var(--accent) 0%, var(--accent-soft) 40%, var(--accent-glint) 55%, var(--accent-soft) 70%, var(--accent) 100%);
  }
  .card--front .band--left { top: 148px; left: 0; width: 218px; }
  .card--front .band--right { top: 148px; left: 342px; width: 218px; }

  .brand-dot {
    position: absolute;
    left: 234px;
    top: 86px;
    width: 92px;
    height: 92px;
    border-radius: 50%;
    background: var(--accent);
  }
  .brand-name {
    position: absolute;
    top: 196px;
    left: 0;
    width: 100%;
    text-align: center;
    font-family: "Jura", sans-serif;
    font-weight: 600;
    font-size: 20px;
    letter-spacing: 2px;
    color: var(--accent);
  }
  .brand-tagline {
    position: absolute;
    top: 224px;
    left: 0;
    width: 100%;
    text-align: center;
    font-family: "Arimo", sans-serif;
    font-size: 8px;
    letter-spacing: 1.5px;
    color: var(--text-light);
  }

  .brand-dot--small {
    position: absolute;
    left: 96px;
    top: -14px;
    width: 48px;
    height: 48px;
    border-radius: 50%;
    background: var(--accent);
  }
  .person-name {
    position: absolute;
    top: 50px;
    left: 36px;
    font-family: "Jura", sans-serif;
    font-weight: 400;
    font-size: 42px;
    line-height: 52px;
    letter-spacing: 1px;
    color: var(--accent);
    white-space: nowrap;
  }
  .card--back .band--full { top: 112px; left: 0; width: 100%; }
  .person-title {
    position: absolute;
    top: 132px;
    left: 36px;
    font-family: "Arimo", sans-serif;
    font-size: 15px;
    line-height: 18px;
    letter-spacing: 1px;
    color: var(--accent);
  }
  .contact {
    position: absolute;
    top: 174px;
    left: 36px;
    font-family: "Arimo", sans-serif;
    font-size: 14px;
    line-height: 21px;
    color: var(--accent);
    list-style: none;
    white-space: nowrap;
  }
</style>
</head>
<body>
  <main class="canvas">
    <section class="card card--front" aria-label="Card front">
      <div class="band band--left"></div>
      <div class="band band--right"></div>
      <div class="brand-dot"></div>
      <h1 class="brand-name">GOLD LANTERN STUDIOS</h1>
      <p class="brand-tagline">A MEDIA ENTERTAINMENT COMPANY</p>
    </section>

    <section class="card card--back" aria-label="Card back">
      <div class="brand-dot--small"></div>
      <h2 class="person-name">Peter Dunmore</h2>
      <div class="band band--full"></div>
      <p class="person-title">MANAGING PARTNER</p>
      <ul class="contact">
        <li>KVT Arts Park, 2480 Wexley Boulevard,</li>
        <li>Arts Hall, 4th Floor, Manhattan Beach, CA 90266</li>
        <li>Phone: 310-555-4206</li>
        <li>E-mail: peter@goldlanternstudioshouse.com</li>
        <li>www.goldlanternstudioshouse.com</li>
      </ul>
    </section>
  </main>
</body>
</html>
```